Business Card for Quillmark Ledger - A cannabis publication for executives.

I'd like some business cards for Quillmark Ledger. The logo is done (great job!) and I need a card design I will use with PRINTLY. I made it a short project to allow time for printing before an event. These will be standard sized cards (final artwork size 3.66" x 2.16" at 300dpi) with a final card size of 3.5" x 2.0". (See PRINTLY.com if you need more info.) I might try rounded corners but am not sure yet. I think the design will work okay with rounded.

Quillmark Ledger will be a bi-weekly publication for the cannabis industry. It is targeted to investors and industry executives, not consumers or pot smokers. So our market is more B2B. However I am open to creativity and making the card something people remark on.

My contact for card:

Dana Merrow
Founder/CEO
dana@quillmarkledger.example

2740 Harlow Avenue
Boston MA 02135
(617)555-0194

Target Market(s)

Executives, Industry people and investors in the Cannabis sector.

Contact Information for Business Card

PRINTLY does do double sided and the second side can be the same or different images. Only one side is required but use of the second side would be a bonus.

Font styles to use
Serif
Sans Serif
Decorative

Colors

Designer to choose colors to be used in the design.

Requirements
Must have
• Logo, contact info
Nice to have
• Style and design to make the card stand out in a crowd.

```html
<!DOCTYPE html>
<html lang="en">
<head>
<meta charset="utf-8">
<title>Dana Merrow — Business Card</title>
<link rel="stylesheet" href="https://fonts.googleapis.com/css2?family=Vollkorn:wght@400;600&family=Nunito+Sans:wght@400&display=swap">
<style>
  :root {
    --card-white: #ffffff;
    --edge-black: #1a1a1a;
    --leaf-green: #72d600;
    --ink-blue: #2e7ff0;
  }
  html, body {
    margin: 0;
    padding: 0;
    width: 1200px;
    height: 695px;
    overflow: hidden;
    background: var(--card-white);
  }
  .card {
    position: relative;
    width: 1200px;
    height: 695px;
  }
  .card-art {
    position: absolute;
    inset: 0;
  }
  .card-edge {
    fill: none;
    stroke: var(--edge-black);
    stroke-width: 1.5;
  }
  .side-band {
    fill: var(--leaf-green);
  }
  .brand {
    position: absolute;
    left: 112px;
    top: 66px;
    display: flex;
    align-items: center;
    gap: 16px;
  }
  .brand-square {
    width: 38px;
    height: 38px;
    background: var(--leaf-green);
  }
  .brand-name {
    margin: 0;
    font-family: "Vollkorn", Georgia, serif;
    font-weight: 600;
    font-size: 42px;
    line-height: 48px;
    color: var(--ink-blue);
  }
  .contact-block {
    position: absolute;
    left: 452px;
    top: 334px;
    margin: 0;
  }
  .person-name {
    margin: 0;
    font-family: "Vollkorn", Georgia, serif;
    font-weight: 600;
    font-size: 76px;
    line-height: 82px;
    color: var(--ink-blue);
  }
  .person-title {
    margin: -4px 0 0 0;
    font-family: "Vollkorn", Georgia, serif;
    font-weight: 400;
    font-size: 37px;
    line-height: 44px;
    color: var(--leaf-green);
  }
  .contact-lines {
    margin: 16px 0 0 0;
    font-family: "Nunito Sans", Arial, sans-serif;
    font-size: 30px;
    line-height: 39px;
    color: var(--ink-blue);
    font-style: normal;
  }
  .contact-lines span {
    display: block;
  }
</style>
</head>
<body>
  <main class="card">
    <svg class="card-art" width="1200" height="695" viewBox="0 0 1200 695" aria-hidden="true">
      <defs>
        <clipPath id="card-shape">
          <rect x="11" y="11" width="1178" height="673" rx="50" ry="50"/>
        </clipPath>
      </defs>
      <g clip-path="url(#card-shape)">
        <rect class="side-band" x="11" y="11" width="58" height="673"/>
      </g>
      <rect class="card-edge" x="11" y="11" width="1178" height="673" rx="50" ry="50"/>
    </svg>

    <header class="brand">
      <span class="brand-square" aria-hidden="true"></span>
      <p class="brand-name">Quillmark Ledger</p>
    </header>

    <section class="contact-block">
      <h1 class="person-name">Dana Merrow</h1>
      <p class="person-title">Founder/CEO</p>
      <address class="contact-lines">
        <span class="contact-email">dana@quillmarkledger.example</span>
        <span class="contact-street">2740 Harlow Avenue</span>
        <span class="contact-city">Boston MA 02135</span>
        <span class="contact-phone">(617)555-0194</span>
      </address>
    </section>
  </main>
</body>
</html>
```